Colm Brevik Interior Design

I need a web design/business card design(branding for company as a whole)for a San Francisco based interior design company. Looking for a clean and modern website that is not too modern. I have younger and older clients. I want my website to be easy to use and be able to group my different projects in one area along with having my pictures be the main focus of the website as that is my selling point. I would like my website to be in the black white silver and gold color scheme but open to other colors. I also want the website to feel playful

Target Market(s)

All types. Want the website to feel open and clean but warm at the same time
examples of work I like. http://www.olenstudio.example/ns/portfolio/design.php
Like many of the business card designs on this link. . really like the one card that has the message in it" hello, my name is" http://www.tillerpressworks.example/2011/03/black-business-cards/

http://www.vantor-bay.example/archives/home_2011_12_01.html

These links will give you an idea of the style I like. I want to do a die cut business card and want that type of look on my website as well. Want my branding to feel like a story to my clients. I like the interaction or theme that some of the examples have. I want people to pick up my business cards because the look cool and different. it's the small details that makes in difference in my business and I want that to show in my website and business card- and overall branding.

Industry/Entity Type

Business

Requirements
Must have
• Chatterlane link
Careernest link
plume link to my reviews
zibbo map of my office
snipwallia.example
contact form page

```html
<!DOCTYPE html>
<html lang="en">
<head>
<meta charset="utf-8">
<title>Colm Brevik Interior Design</title>
<link rel="stylesheet" href="https://fonts.googleapis.com/css2?family=Alice&family=Arimo:ital,wght@0,400;0,700;1,400&display=swap">
<style>
:root{
  --black:#000;
  --white:#fff;
  --gold:#e6bd1a;
  --silver-bar:rgba(205,205,205,.85);
  --card-grey:#b4b4b4;
  --text-grey:#8a8a8a;
  --rule:#bdbdbd;
  --read-more:#4a4a4a;
  --brand-ink:#111;
}
*{margin:0;padding:0;box-sizing:border-box}
html,body{width:1200px;height:1028px;overflow:hidden;background:var(--black)}
body{position:relative;font-family:"Arimo",Arial,sans-serif}
.backdrop{position:absolute;left:0;top:0;width:1200px;height:500px;
  background:linear-gradient(180deg,#cfcfcf 0%,#bdbdbd 20%,#8a8a8a 38%,#3a3a3a 62%,#000 92%)}
.brand{position:absolute;left:203px;top:14px;width:299px;height:66px;
  display:flex;align-items:center;justify-content:center}
.brand-name{color:var(--brand-ink);font-weight:700;font-size:23px;line-height:32px;text-align:center;letter-spacing:.5px}
.social{position:absolute;left:812px;top:47px;display:flex;gap:9px;list-style:none}
.social a{display:flex;align-items:center;font-size:10px;color:var(--white);text-decoration:none;
  background:#555;padding:0 5px;height:26px;border-radius:2px}
.nav{position:absolute;left:0;top:128px;width:1200px;height:34px;background:var(--silver-bar)}
.nav a{position:absolute;top:0;line-height:34px;font-size:16.5px;color:var(--white);text-decoration:none}
.nav .sep{position:absolute;top:8px;width:1px;height:21px;background:var(--white)}
.slide{position:absolute;border:2px dashed var(--white)}
.slide-left{left:203px;top:233px;width:212px;height:223px;background:linear-gradient(135deg,#7a4a2a,#c9b9a0 55%,#4c5a3a)}
.slide-right{left:788px;top:233px;width:237px;height:223px;background:linear-gradient(135deg,#c47d4e,#e9d9c0 45%,#3b2a1e)}
.slide-center{left:413px;top:220px;width:376px;height:251px;z-index:2;background:linear-gradient(135deg,#5e4c3e,#c9a87a 40%,#8fa06a 70%,#d8d0b8)}
.main{position:absolute;left:196px;top:485px;width:833px;height:458px;background:var(--white)}
.welcome{position:absolute;left:0;top:18px;width:316px;height:23px;background:var(--gold);
  color:var(--white);font-size:15px;font-weight:400;line-height:24px;padding-left:21px}
.intro{position:absolute;left:21px;top:56px;width:795px;font-size:9.8px;line-height:12px;color:var(--text-grey)}
.intro p+p{margin-top:12px}
.rule{position:absolute;left:18px;top:173px;width:804px;height:1px;background:var(--rule)}
.card{position:absolute;top:186px;width:184px;height:257px;background:var(--card-grey)}
.card-photo{height:94px}
.card-title{height:28px;background:var(--gold);color:var(--white);font-family:"Alice",Georgia,serif;
  font-weight:400;font-size:19px;line-height:29px;text-align:center}
.card-text{padding:5px 6px 0 9px;font-size:9.8px;line-height:12px;color:var(--white)}
.read-more{position:absolute;right:7px;bottom:3px;font-family:"Alice",Georgia,serif;font-style:italic;
  font-size:11px;color:var(--read-more)}
.footer{position:absolute;left:196px;top:952px;width:833px;height:20px;background:var(--white);
  font-size:10px;line-height:20px;color:var(--text-grey);padding-left:11px}
</style>
</head>
<body>
<div class="backdrop" role="img" aria-label="Soft-focus interior room with white tiled wall and red accents"></div>

<header>
  <div class="brand"><div class="brand-name">COLM BREVIK<br>Interior Design</div></div>
  <ul class="social">
    <li><a href="#">Chatterlane</a></li>
    <li><a href="#">zibbo</a></li>
    <li><a href="#">Careernest</a></li>
    <li><a href="#">snipwallia</a></li>
    <li><a href="#">plume</a></li>
  </ul>
  <nav class="nav">
    <a href="#" style="left:206px">Home</a><span class="sep" style="left:279px"></span>
    <a href="#" style="left:320px">About Us</a><span class="sep" style="left:423px"></span>
    <a href="#" style="left:468px">Interior Designs</a><span class="sep" style="left:628px"></span>
    <a href="#" style="left:661px">Products</a><span class="sep" style="left:761px"></span>
    <a href="#" style="left:795px">Services</a><span class="sep" style="left:894px"></span>
    <a href="#" style="left:926px">Contact Us</a>
  </nav>
</header>

<section class="slider">
  <div class="slide slide-left" role="img" aria-label="Living room with wood panelling, white sofa and painting"></div>
  <div class="slide slide-center" role="img" aria-label="Designer sorting tile and fabric samples on a table"></div>
  <div class="slide slide-right" role="img" aria-label="Sunroom with tall windows and wicker furniture"></div>
</section>

<main class="main">
  <h1 class="welcome">Welcome to Colm Brevik Interior Design</h1>
  <div class="intro">
    <p>There are many variations of passages of Lorem Ipsum available, but the majority have suffered alteration in some form, by injected humour, or randomised words which don't look even slightly believable. If you are going to use a passage of Lorem Ipsum, you need to be sure there isn't anything embarrassing hidden in the middle of text. All the Lorem Ipsum generators on the Internet tend to repeat predefined chunks as necessary, making this the first true generator on the Internet. It uses a dictionary of over 200 Latin words, combined with a handful of model sentence structures, to generate Lorem Ipsum which looks reasonable. The generated Lorem Ipsum is therefore always free from repetition, injected humour, or non-characteristic words etc.</p>
    <p>The standard chunk of Lorem Ipsum used since the 1500s is reproduced below for those interested. Sections 1.10.32 and 1.10.33 from “de Finibus Bonorum et Malorum” by Tullan Varro are also reproduced in their exact original form, accompanied by English versions from the 1914 translation by H. Ransford.</p>
  </div>
  <div class="rule"></div>

  <article class="card" style="left:18px">
    <div class="card-photo" role="img" aria-label="Modern washroom with stone wall" style="background:linear-gradient(135deg,#d9cfc2,#9a7a5a)"></div>
    <h2 class="card-title">Washrooms</h2>
    <p class="card-text">Lorem ipsum dolor sit amet, consectetur adipisicing elit, sed do eiusmod tempor incididunt ut labore et dolore magna aliqua. Ut enim ad minim veniam, quis nostrud exercitation ullamco laboris nisi ut aliquip ex ea commodo consequat. Duis aute irure dolor in reprehenderit in voluptate velit esse cillum dolore eu fugiat nulla pariatur.</p>
    <a class="read-more">read more</a>
  </article>
  <article class="card" style="left:225px">
    <div class="card-photo" role="img" aria-label="Kitchen with wooden cabinets and island" style="background:linear-gradient(135deg,#8a5a32,#c9a780 60%,#5a3a22)"></div>
    <h2 class="card-title">Kitchens</h2>
    <p class="card-text">Lorem ipsum dolor sit amet, consectetur adipisicing elit, sed do eiusmod tempor incididunt ut labore et dolore magna aliqua. Ut enim ad minim veniam, quis nostrud exercitation ullamco laboris nisi ut aliquip ex ea commodo consequat. Duis aute irure dolor in reprehenderit in voluptate velit esse cillum dolore eu fugiat nulla pariatur.</p>
    <a class="read-more">read more</a>
  </article>
  <article class="card" style="left:431px">
    <div class="card-photo" role="img" aria-label="Tiler setting wall tiles on adhesive" style="background:linear-gradient(135deg,#e8e8e4,#8a8a5a 60%,#6e6e44)"></div>
    <h2 class="card-title">Walls</h2>
    <p class="card-text">Lorem ipsum dolor sit amet, consectetur adipisicing elit, sed do eiusmod tempor incididunt ut labore et dolore magna aliqua. Ut enim ad minim veniam, quis nostrud exercitation ullamco laboris nisi ut aliquip ex ea commodo consequat. Duis aute irure dolor in reprehenderit in voluptate velit esse cillum dolore eu fugiat nulla pariatur.</p>
    <a class="read-more">read more</a>
  </article>
  <article class="card" style="left:638px;height:261px">
    <div class="card-photo" role="img" aria-label="Living room with shelving and fireplace" style="height:97px;background:linear-gradient(135deg,#7a4426,#c8a682 55%,#6a4a30)"></div>
    <h2 class="card-title">Living Room</h2>
    <p class="card-text">Lorem ipsum dolor sit amet, consectetur adipisicing elit, sed do eiusmod tempor incididunt ut labore et dolore magna aliqua. Ut enim ad minim veniam, quis nostrud exercitation ullamco laboris nisi ut aliquip ex ea commodo consequat. Duis aute irure dolor in reprehenderit in voluptate velit esse cillum dolore eu fugiat nulla pariatur.</p>
    <a class="read-more">read more</a>
  </article>
</main>

<footer class="footer">Copyright © 2012 colm brevik interior design. All rights reserved</footer>
</body>
</html>
```